Varnel Consulting needs a business card design

Varnel Consulting is a small business that consults and trains Australia wide in Workplace Health and Safety, Environment and Quality Management Systems.

Clients are typically smaller businesses with 50 to 200 employees but there are some large clients.

Communication is often by email, although mobile is used as well.

Varnel Consulting
61 Tormoth Vale Road
Pellowby, QLD 4391
0438 912 047

```html
<!DOCTYPE html>
<html lang="en">
<head>
<meta charset="utf-8">
<title>Varnel Consulting – Business Card</title>
<link rel="stylesheet" href="https://fonts.googleapis.com/css2?family=Barlow:wght@300;400&display=swap">
<style>
  :root {
    --page-bg: #e9eaec;
    --navy-deep: #0a1836;
    --blue-bright: #15579a;
    --blue-soft: #1a5ea3;
    --text-white: #ffffff;
    --mark-grey: #9c9ea3;
    --card-shadow: rgba(0, 0, 0, 0.35);
  }
  html, body {
    margin: 0;
    padding: 0;
    width: 1200px;
    height: 1200px;
    overflow: hidden;
    background: var(--page-bg);
  }
  .canvas {
    position: relative;
    width: 1200px;
    height: 1200px;
  }
  .business-card {
    position: absolute;
    left: 50px;
    top: 298px;
    width: 1100px;
    height: 604px;
    overflow: hidden;
    box-shadow: 0 18px 30px var(--card-shadow);
    font-family: "Barlow", "Helvetica Neue", Arial, sans-serif;
    color: var(--text-white);
  }
  .card-backdrop {
    position: absolute;
    inset: 0;
    background: linear-gradient(110deg, var(--blue-soft) 0%, var(--navy-deep) 40%, var(--navy-deep) 55%, var(--blue-bright) 100%);
  }
  .brand {
    position: absolute;
    left: 62px;
    top: 118px;
    display: flex;
    align-items: center;
    gap: 18px;
  }
  .brand-dot {
    width: 44px;
    height: 44px;
    border-radius: 50%;
    background: var(--mark-grey);
  }
  .brand-name {
    font-weight: 300;
    font-size: 40px;
    letter-spacing: 0.5px;
    color: var(--text-white);
  }
  .holder-name {
    position: absolute;
    right: 87px;
    top: 205px;
    margin: 0;
    font-weight: 300;
    font-size: 84px;
    letter-spacing: 1.5px;
    line-height: 1;
  }
  .contact-details {
    position: absolute;
    left: 45px;
    top: 398px;
    margin: 0;
    font-style: normal;
    font-weight: 300;
    font-size: 32px;
    line-height: 41px;
  }
</style>
</head>
<body>
<main class="canvas">
  <section class="business-card">
    <div class="card-backdrop" role="img" aria-label="Decorative flowing wave background in navy and blue"></div>

    <div class="brand">
      <span class="brand-dot"></span>
      <span class="brand-name">Varnel Consulting</span>
    </div>

    <h1 class="holder-name">Ewan Marlow</h1>

    <address class="contact-details">
      Varnel Consulting<br>
      61 Tormoth Vale Road<br>
      Pellowby, QLD 4391<br>
      0438 912 047
    </address>
  </section>
</main>
</body>
</html>
```